Dental clinic brochure design (Z fold)

We need a new brochure design made for our dental clinic - Brindlemoor Dental Surgery. One side is in English, the other is in Vietnamese - all text and translations provided in brochure sample with further instructions in word doc. We require a brochure design in a Z fold to convey a family friendly dental clinic, incorporating our logo colour into the theme and designers choice on complimentary colours. Additional high quality images are provided for use if required or free to use own images.

Colors
33b8a4
00a990
86cfc6

Requirements
Must have
• Easy to read font, flows from text to pictures and page to page
• At least 2 dental images

```html
<!DOCTYPE html>
<html lang="en">
<head>
<meta charset="utf-8">
<title>Brindlemoor Dental Surgery – Brochure</title>
<link href="https://fonts.googleapis.com/css2?family=Open+Sans:wght@400;600;700&display=swap" rel="stylesheet">
<style>
  :root {
    --teal: #2bbcaa;
    --teal-deep: #00a990;
    --teal-soft: #86cfc6;
    --ink: #3b3b3b;
    --white: #ffffff;
  }
  * { margin: 0; padding: 0; box-sizing: border-box; }
  html, body { width: 1200px; height: 1000px; overflow: hidden; background: var(--white); }
  body { font-family: "Open Sans", Arial, sans-serif; color: var(--ink); }
  .brochure { position: relative; width: 1200px; height: 1000px; }
  .panel { position: absolute; }
  .teal { background: var(--teal); }

  .pill {
    position: absolute; border-radius: 60px;
    font-weight: 700; font-size: 26px; line-height: 34px;
    display: flex; align-items: center; letter-spacing: 0.2px;
  }
  .pill--white { background: var(--white); color: var(--teal); left: 55px; top: 57px; width: 314px; height: 106px; padding-left: 36px; }
  .pill--teal { background: var(--teal); color: var(--white); left: 40px; top: 57px; width: 313px; height: 106px; padding-left: 46px; }

  .lead-dark { color: #333; text-shadow: 0 0 2px rgba(255,255,255,0.9), 0 0 1px #fff; font-size: 22px; line-height: 31px; }
  .body-copy { font-size: 22px; line-height: 30px; color: #333; }

  .photo { position: absolute; }
  .photo--kids { left: 0; top: 362px; width: 405px; height: 272px;
    background: radial-gradient(ellipse at 50% 60%, #f0c9a8 0%, #e9d36a 35%, #f3f3f3 75%, #fff 100%); }
  .photo--smile { left: 405px; top: 368px; width: 392px; height: 260px;
    background: radial-gradient(ellipse at 50% 55%, #f2cbb0 0%, #c79c78 40%, #7d7f84 80%, #5d6066 100%); }
  .map { left: 840px; top: 368px; width: 318px; height: 262px; background: #f1f2f2; border: 1px solid #d6d6d6; }

  .doctors { position: absolute; left: 38px; top: 53px; color: var(--white); font-size: 17px; line-height: 24px; }
  .doctors li { list-style: none; margin-bottom: 9px; }

  .address { position: absolute; left: 61px; top: 80px; color: var(--white); font-size: 15px; line-height: 21px; }
  .address h2 { font-size: 19px; font-weight: 700; margin-bottom: 15px; letter-spacing: 0.3px; }

  .fineprint { font-size: 15px; line-height: 22px; color: #333; }
</style>
</head>
<body>
<main class="brochure">

  <!-- Left column -->
  <section class="panel teal" style="left:0;top:73px;width:405px;height:289px;">
    <div class="pill pill--white">CHILD DENTAL<br>BENEFITS SCHEME</div>
    <p class="lead-dark" style="position:absolute;left:52px;top:183px;width:300px;">A dental benefits program is available for eligible children aged 2 to 17 and</p>
  </section>
  <div class="photo photo--kids" role="img" aria-label="Group of smiling children brushing their teeth"></div>
  <section class="panel teal" style="left:0;top:634px;width:405px;height:293px;">
    <p class="lead-dark" style="position:absolute;left:65px;top:14px;width:300px;">will <strong>receive $1000</strong> for dental treatments.</p>
    <svg style="position:absolute;left:60px;top:126px;" width="56" height="76" viewBox="0 0 56 76" aria-hidden="true">
      <path d="M14 4 L24 20 Q26 24 22 27 L17 31 Q19 44 31 55 L36 51 Q40 48 43 51 L54 64 Q56 67 52 70 L46 74 Q38 78 26 66 Q6 46 3 24 Q1 10 8 5 L10 3 Q12 2 14 4 Z" fill="#ffffff"/>
    </svg>
    <p class="lead-dark" style="position:absolute;left:133px;top:112px;width:240px;">To check if your children are eligible call us on 9000 4812.</p>
  </section>

  <!-- Middle column -->
  <section class="panel" style="left:405px;top:73px;width:392px;height:289px;">
    <div class="pill pill--teal">SPECIAL<br>PROMOTIONS</div>
    <p class="body-copy" style="position:absolute;left:31px;top:183px;width:340px;">Gap free dental check-up, clean &amp; x-rays for all health insurances**</p>
  </section>
  <div class="photo photo--smile" role="img" aria-label="Smiling girl with glasses and braces"></div>
  <section class="panel" style="left:405px;top:634px;width:392px;height:293px;">
    <p class="body-copy" style="position:absolute;left:31px;top:17px;width:330px;">At home whitening kit now $199 limited time only (normally $395).</p>
    <p class="body-copy" style="position:absolute;left:31px;top:122px;width:330px;">Braces, dentures and implants are available at our clinic.</p>
    <p class="fineprint" style="position:absolute;left:31px;top:189px;width:330px;">**Conditions apply—Ask staff for more information</p>
  </section>

  <!-- Right column -->
  <section class="panel teal" style="left:797px;top:73px;width:403px;height:289px;">
    <ul class="doctors">
      <li>Dr Alan Vo BDSc (Melb), ICCDE</li>
      <li>Dr Minh Tran BDSc (Melb), FICCDE<br>FRACDS, PGradDipCD Implants (Melb)</li>
      <li>Dr Linh Nguyen BHsc Mdent (Latrobe)</li>
      <li>Dr Daniel Ho BHsc Mdent (Latrobe),<br>FRACDS</li>
      <li>Dr Mai Do BDS (Adl)</li>
    </ul>
  </section>
  <div class="photo map" role="img" aria-label="Street map showing the clinic location"></div>
  <section class="panel teal" style="left:797px;top:634px;width:403px;height:293px;">
    <div class="address">
      <h2>PRIMARY BUSINESS ADDRESS</h2>
      <p>48 Larkfield Road<br>Ashbury, VIC 3099<br>Phone: (03) 9000 4812<br>Email: admin@brindlemoordental.com.au</p>
    </div>
  </section>

</main>
</body>
</html>
```